Award-winnning Estate Agent needs a premium version of their 'For Sale' board design

We need a premium option for our 'For Sale' board design. We have a standard board that is attached to this brief, but were are looking to have a premium design version that we will use when selling exclusive properties. Our company name is Harbour Lane Estates and the name for this is exclusive selection is: 'The Harbour Collection'. The design needs to work with our current brand, but have a distinctive PREMIUM feel to it. I have uploaded the barnd guidelines and also some of the exisisting logo variations. We do NOT need a new logo but feel free to play around with colours, fonts, sizes etc. for the sign.

Target Market(s)

Property buyers & house hunters

Industry/Entity Type

Real Estate - Residential Property

Font styles to use
Sans Serif

Requirements
Must have
• A premium fee, must be square design, must be easy to read when driving past the sign
Nice to have
• I'm open ot ideas

```html
<!DOCTYPE html>
<html lang="en">
<head>
<meta charset="utf-8">
<title>Harbour Lane Estates – For Sale Board</title>
<link href="https://fonts.googleapis.com/css2?family=Montserrat:wght@500;700;800&display=swap" rel="stylesheet">
<style>
  :root {
    --navy: #1b2583;
    --blue: #2161b3;
    --sky: #2b93d6;
    --white: #ffffff;
    --backdrop: #e9e9ec;
    --edge: #d6d6dc;
  }
  * { box-sizing: border-box; margin: 0; padding: 0; }
  html, body {
    width: 1200px;
    height: 675px;
    overflow: hidden;
    background: var(--backdrop);
    font-family: "Montserrat", Arial, sans-serif;
  }
  .board {
    position: absolute;
    left: 295px;
    top: 32px;
    width: 610px;
    height: 610px;
    background: var(--white);
    border: 2px solid var(--edge);
    overflow: hidden;
  }
  .brand {
    position: absolute;
    left: 28px;
    top: 34px;
    display: flex;
    align-items: center;
    gap: 12px;
  }
  .brand-square {
    width: 42px;
    height: 42px;
    background: var(--blue);
  }
  .brand-name {
    color: var(--blue);
    font-weight: 500;
    font-size: 24px;
    line-height: 1.05;
  }
  .corner-flag {
    position: absolute;
    left: 0;
    top: 0;
  }
  .collection-title {
    position: absolute;
    left: 0;
    right: 0;
    top: 156px;
    text-align: center;
    color: var(--blue);
    font-weight: 800;
    font-size: 29px;
    letter-spacing: 0.3px;
    text-transform: uppercase;
  }
  .for-sale {
    position: absolute;
    left: 0;
    right: 0;
    top: 206px;
    display: flex;
    justify-content: center;
    align-items: center;
    gap: 18px;
  }
  .for-word {
    color: var(--navy);
    font-weight: 800;
    font-size: 84px;
    line-height: 1;
  }
  .sale-word {
    background: var(--sky);
    color: var(--white);
    font-weight: 800;
    font-size: 84px;
    line-height: 1;
    padding: 10px 20px 8px;
  }
  .skyline-upper {
    position: absolute;
    left: 430px;
    top: 302px;
    width: 142px;
    height: 70px;
  }
  .phone-band {
    position: absolute;
    left: 0;
    right: 0;
    top: 372px;
    height: 54px;
    background: var(--blue);
    display: flex;
    align-items: center;
    padding-left: 32px;
    gap: 28px;
  }
  .phone-icon { flex: none; }
  .phone-number {
    color: var(--white);
    font-weight: 700;
    font-size: 33px;
    letter-spacing: 1px;
  }
  .web-band {
    position: absolute;
    left: 0;
    right: 0;
    top: 438px;
    height: 160px;
    background: var(--navy);
  }
  .web-address {
    position: absolute;
    left: 0;
    right: 0;
    top: 16px;
    text-align: center;
    color: var(--white);
    font-weight: 700;
    font-size: 27px;
  }
  .skyline-lower {
    position: absolute;
    left: 0;
    right: 0;
    top: 74px;
    height: 86px;
  }
</style>
</head>
<body>
  <main class="board">
    <svg class="corner-flag" width="610" height="140" viewBox="0 0 610 140" aria-hidden="true">
      <polygon points="354,10 574,10 574,132" fill="var(--blue)"/>
    </svg>

    <div class="brand">
      <span class="brand-square"></span>
      <span class="brand-name">Harbour Lane<br>Estates</span>
    </div>

    <h1 class="collection-title">The Harbour Collection</h1>

    <div class="for-sale">
      <span class="for-word">FOR</span>
      <span class="sale-word">SALE</span>
    </div>

    <svg class="skyline-upper" viewBox="0 0 142 70" role="img" aria-label="Town skyline silhouette with clock tower">
      <defs>
        <linearGradient id="upperTone" x1="0" y1="0" x2="0" y2="1">
          <stop offset="0" stop-color="#2b6fc0"/>
          <stop offset="1" stop-color="#1f57a8"/>
        </linearGradient>
      </defs>
      <rect width="142" height="70" fill="url(#upperTone)"/>
    </svg>

    <div class="phone-band">
      <svg class="phone-icon" width="40" height="40" viewBox="0 0 40 40" aria-hidden="true">
        <circle cx="20" cy="20" r="19" fill="var(--navy)"/>
        <path d="M14 11c1-.6 2-.4 2.6.5l2 3c.5.8.3 1.7-.4 2.2l-1.3 1c.8 2 2.4 3.6 4.4 4.4l1-1.3c.5-.7 1.4-.9 2.2-.4l3 2c.9.6 1.1 1.6.5 2.6l-1 1.5c-.7 1-2 1.5-3.2 1.1C17.7 26 14 22.3 12.4 16.2c-.4-1.2.1-2.5 1.1-3.2z" fill="var(--white)"/>
      </svg>
      <span class="phone-number">01632 960482</span>
    </div>

    <section class="web-band">
      <p class="web-address">www.harbourlaneestates.co.uk</p>
      <svg class="skyline-lower" viewBox="0 0 610 86" preserveAspectRatio="none" role="img" aria-label="Row of town buildings and towers along the base of the board">
        <defs>
          <linearGradient id="lowerTone" x1="0" y1="0" x2="0" y2="1">
            <stop offset="0" stop-color="#1f3f9e"/>
            <stop offset="1" stop-color="#2161b3"/>
          </linearGradient>
        </defs>
        <rect width="610" height="86" fill="url(#lowerTone)"/>
      </svg>
    </section>
  </main>
</body>
</html>
```